Postcard Design

Breeze Haven Services Inc. is a Air duct cleaning, dryer vent cleaning & pressure washing company, FVRQ certified company. Family owned started in 2007.

Target Market(s)

Have large amount of calls for these specials

Industry/Entity Type

Pressure Cleaning

Font styles to use
Serif

Requirements
Must have
• Would like to have a special of $295.00 entire home & patio or deck, and also a special offer for a $245.00 air duct cleaning, dryer vent cleaning & sanitation package.
Nice to have
• really want the summer time feeling on the card

```html
<!DOCTYPE html>
<html lang="en">
<head>
<meta charset="utf-8">
<title>Breeze Haven Services – Postcard</title>
<link rel="stylesheet" href="https://fonts.googleapis.com/css2?family=Archivo+Black&family=Source+Sans+3:ital,wght@0,400;0,600;0,700;1,600;1,700&display=swap">
<style>
  :root {
    --orange: #f7a552;
    --teal: #6ccbd1;
    --white: #ffffff;
    --brown: #b5562a;
    --red-orange: #e2582a;
    --gold: #f59b2c;
    --yellow: #fbe07a;
    --check: #7fd0ea;
    --photo-wood: #b9793f;
    --photo-wall: #e9e2d6;
    --duct-dark: #4a4a46;
    --duct-light: #b8bcbd;
  }
  * { margin: 0; padding: 0; box-sizing: border-box; }
  html, body { width: 1200px; height: 706px; overflow: hidden; background: #ffffff; }
  .postcard {
    position: relative;
    width: 1200px;
    height: 706px;
    overflow: hidden;
    background: var(--orange);
    font-family: "Source Sans 3", "Myriad Pro", Arial, sans-serif;
  }
  .backdrop { position: absolute; inset: 0; }
  .brand {
    position: absolute;
    left: 70px;
    top: 100px;
    width: 487px;
    text-align: center;
    color: var(--teal);
    font-weight: 700;
    font-size: 47px;
    line-height: 1;
  }
  .tagline {
    position: absolute;
    left: 62px;
    top: 210px;
    width: 495px;
    text-align: center;
    font-family: "Archivo Black", Impact, sans-serif;
    font-size: 17px;
    letter-spacing: 2px;
    color: var(--brown);
    white-space: nowrap;
  }
  .services-title {
    position: absolute;
    left: 54px;
    top: 280px;
    color: var(--white);
    font-weight: 600;
    font-size: 33px;
  }
  .services-list { position: absolute; left: 54px; top: 330px; list-style: none; }
  .services-list li {
    display: flex;
    align-items: center;
    height: 53px;
    color: var(--white);
    font-weight: 600;
    font-size: 29px;
  }
  .services-list svg { width: 26px; height: 26px; margin-right: 28px; }
  .estimate-call {
    position: absolute;
    left: 60px;
    top: 540px;
    width: 400px;
    text-align: center;
    color: var(--red-orange);
    font-weight: 600;
    font-size: 21px;
  }
  .phone {
    position: absolute;
    left: 76px;
    top: 584px;
    width: 354px;
    height: 62px;
    border-radius: 10px;
    background: var(--teal);
    border: 2px dashed rgba(255,255,255,0.55);
    display: flex;
    align-items: center;
    justify-content: center;
    gap: 12px;
    color: var(--white);
    font-weight: 700;
    font-size: 38px;
  }
  .phone svg { width: 34px; height: 34px; }
  .before-after {
    position: absolute;
    left: 567px;
    top: 160px;
    width: 220px;
    height: 220px;
    border-radius: 50%;
    border: 8px solid var(--white);
    overflow: hidden;
    background: linear-gradient(135deg, var(--duct-dark) 0%, #6c6b66 49.6%, #ffffff 50%, var(--duct-light) 50.4%, #8f9597 100%);
  }
  .before-after span {
    position: absolute;
    color: var(--white);
    font-weight: 600;
    font-size: 18px;
  }
  .before-after .before { left: 16px; top: 70px; }
  .before-after .after { right: 22px; top: 132px; }
  .guarantee {
    position: absolute;
    left: 540px;
    top: 428px;
    width: 300px;
    text-align: center;
    color: var(--gold);
    font-style: italic;
    font-weight: 700;
    font-size: 21px;
  }
  .family {
    position: absolute;
    left: 540px;
    top: 458px;
    width: 300px;
    text-align: center;
    color: var(--white);
    font-style: italic;
    font-weight: 600;
    font-size: 21px;
  }
  .offer {
    position: absolute;
    top: 541px;
    width: 254px;
    height: 127px;
    border-radius: 16px;
    background: var(--yellow);
    border: 4px solid var(--white);
    text-align: center;
    color: var(--red-orange);
    padding-top: 6px;
  }
  .offer-home { left: 555px; }
  .offer-package { left: 841px; }
  .offer-label { font-weight: 700; font-size: 18px; }
  .offer-price { font-weight: 700; font-size: 38px; line-height: 1.1; }
  .offer-detail { font-size: 15px; line-height: 1.1; margin-top: 4px; }
  .badge {
    position: absolute;
    left: 1103px;
    top: 31px;
    width: 73px;
    height: 124px;
    border-radius: 5px;
    background: var(--white);
    border: 2px solid #d8d8d8;
  }
</style>
</head>
<body>
<div class="postcard">
  <svg class="backdrop" viewBox="0 0 1200 706" width="1200" height="706" aria-hidden="true">
    <path d="M660 0 C610 70 570 170 560 260 C550 350 488 380 490 470 C492 560 510 640 520 706 L1200 706 L1200 0 Z" fill="var(--white)"/>
    <path d="M695 0 C645 70 605 170 595 260 C585 350 520 380 520 470 C522 560 540 640 550 706 L1200 706 L1200 0 Z" fill="var(--teal)"/>
    <path d="M772 330 C880 440 1040 492 1200 500 L1200 548 C1030 545 860 480 772 380 Z" fill="var(--white)"/>
  </svg>
  <svg class="backdrop" viewBox="0 0 1200 706" width="1200" height="706" role="img" aria-label="Photo of hands vacuuming a floor air vent with a black hose">
    <defs>
      <linearGradient id="photoTone" x1="0" y1="0" x2="1" y2="1">
        <stop offset="0" stop-color="var(--photo-wall)"/>
        <stop offset="0.35" stop-color="var(--photo-wood)"/>
        <stop offset="1" stop-color="#a3632f"/>
      </linearGradient>
    </defs>
    <path d="M745 0 L1200 0 L1200 482 C1040 476 880 436 800 348 C744 280 726 150 745 0 Z" fill="url(#photoTone)" stroke="var(--white)" stroke-width="10"/>
  </svg>

  <div class="brand">Breeze Haven Services</div>
  <div class="tagline">AIR DUCT &amp; DRYER VENT CLEANING</div>

  <div class="services-title">SPECIALIZING IN:</div>
  <ul class="services-list">
    <li><svg viewBox="0 0 26 26" aria-hidden="true"><circle cx="13" cy="13" r="13" fill="var(--check)"/><path d="M7 13.5 L11.5 18 L19 9" fill="none" stroke="var(--white)" stroke-width="3" stroke-linecap="round" stroke-linejoin="round"/></svg>Air Duct Cleaning</li>
    <li><svg viewBox="0 0 26 26" aria-hidden="true"><circle cx="13" cy="13" r="13" fill="var(--check)"/><path d="M7 13.5 L11.5 18 L19 9" fill="none" stroke="var(--white)" stroke-width="3" stroke-linecap="round" stroke-linejoin="round"/></svg>Dryer Vent Cleaning</li>
    <li><svg viewBox="0 0 26 26" aria-hidden="true"><circle cx="13" cy="13" r="13" fill="var(--check)"/><path d="M7 13.5 L11.5 18 L19 9" fill="none" stroke="var(--white)" stroke-width="3" stroke-linecap="round" stroke-linejoin="round"/></svg>Pressure Washing</li>
  </ul>

  <div class="estimate-call">CALL US NOW FOR A FREE ESTIMATE!</div>
  <div class="phone">
    <svg viewBox="0 0 34 34" aria-hidden="true"><circle cx="17" cy="17" r="15" fill="none" stroke="var(--white)" stroke-width="2.5"/><path d="M11.5 9.5 l3 -0.5 l1.8 4.2 l-2 1.6 c1 2.3 2.6 3.9 4.9 4.9 l1.6 -2 l4.2 1.8 l-0.5 3 c-0.3 1 -1.2 1.5 -2.2 1.4 c-6.5 -0.8 -11.2 -5.5 -12 -12 c-0.1 -1 0.4 -1.9 1.2 -2.4 z" fill="var(--white)"/></svg>
    215-555-0148
  </div>

  <div class="before-after" role="img" aria-label="Split photo of a duct interior, dusty before and clean after cleaning">
    <span class="before">BEFORE</span>
    <span class="after">AFTER</span>
  </div>

  <div class="guarantee">ALL WORK IS GUARANTEED!!!</div>
  <div class="family">Family owned started in 2007</div>

  <div class="offer offer-home">
    <div class="offer-label">- SPECIAL OFFER -</div>
    <div class="offer-price">$295.00 of</div>
    <div class="offer-detail">entire home &amp; patio or deck</div>
  </div>
  <div class="offer offer-package">
    <div class="offer-label">- SPECIAL OFFER -</div>
    <div class="offer-price">$245.00 of</div>
    <div class="offer-detail">air duct cleaning, dryer vent<br>cleaning &amp; sanitation package</div>
  </div>

  <div class="badge" role="img" aria-label="FVRQ certification badge"></div>
</div>
</body>
</html>
```